trading data display webpage

We have build a rough wireframe of the two webpages that we want to display .The two wireframes are attached as a pdf document.
there will be login page. after login , the user will see the index page. that is the first page of the wireframe.

what we are displaying is essentially spread data. we are taking the difference in prices are two places and displaying the data. some calculations are done and is shown in the grid.

below the grid we show the behaviour on a graph. we will use bubble chart. I did not find a sample, hence have thrown in a placeholder.

this is time series data ( changes daily) and hence we need to check the behaviour.

the second wire frame shows how the user will choose the source price points and the destination price points.
we are talking here of natural gas prices hence the reference to source prices and destination prices.

you need to design the page/ pages such that the end-user loves it and is easy to use. the intent here is easy to use and easy to understand.
this will be responsive webpage since the end user will check it out on a tablet or a smartphone.

so if possible tell us how the navigation bar, the button bar, etc should fall when the screen size decreases.

I have uploaded 2 files. one is the wireframe ( pdf document) and second is the logo file.

please also let us know where to place the logo.

Target Market(s)

the target market is traders and data analyst

Industry/Entity Type

Build

Colors

Designer to choose colors to be used in the design.

Requirements
Must have
• 1. design for the web.
2. but think how the design will look when the screen size decreases.
3. tell if possible what screen components to keep and what to hide.

```html
<!DOCTYPE html>
<html lang="en">
<head>
<meta charset="utf-8">
<title>GasSpread – Spread Dashboard</title>
<link rel="stylesheet" href="https://fonts.googleapis.com/css2?family=Roboto:wght@300;400;500;700&display=swap">
<style>
  :root{
    --bg:#f1f2f4;
    --panel:#ffffff;
    --line:#e2e3e6;
    --label-bg:#f6f6f7;
    --text:#333333;
    --muted:#777777;
    --green:#7bbd3a;
    --green-dark:#5f9e26;
    --green-light:#d6ebc3;
    --orange:#f26a21;
    --peach:#fbd9c5;
    --pink:#e91e63;
    --grey-bar:#efefef;
    --band:#f5f6f7;
  }
  *{box-sizing:border-box;margin:0;padding:0}
  html,body{width:1200px;height:4500px;overflow:hidden;background:var(--bg)}
  body{font-family:"Roboto",Arial,sans-serif;color:var(--text)}
  .page{width:320px;transform:scale(3.75);transform-origin:0 0;padding-top:4px}

  /* header */
  .site-header{position:relative;height:74px}
  .brand{position:absolute;left:12px;top:22px;display:flex;align-items:center;gap:4px}
  .brand-dot{width:9px;height:9px;border-radius:50%;background:var(--green)}
  .brand-name{font-size:14px;font-weight:700;color:var(--green-dark)}
  .user-greeting{position:absolute;left:188px;top:27px;font-size:8px;color:var(--text);display:flex;align-items:center;gap:2px}
  .options-btn{position:absolute;left:229px;top:19px;width:80px;height:22px;border:1px solid #c9c9c9;border-radius:3px;background:#f7f7f7;font-size:9px;font-weight:500;display:flex;align-items:center;justify-content:center;gap:4px}
  .region-tabs{position:absolute;left:98px;top:54px;display:flex;gap:1px}
  .region-tab{height:20px;font-size:9px;font-weight:700;display:flex;align-items:center;justify-content:center;color:#fff}
  .region-tab.is-active{width:66px;background:var(--panel);color:var(--green);border-top:2px solid var(--green)}
  .region-tab.central{width:75px;background:var(--orange);margin-left:1px}
  .region-tab.west{width:63px;background:var(--pink);margin-left:5px}

  /* main panel */
  .panel{margin:0 10px;background:var(--panel);padding:9px 5px 0;box-shadow:0 0 2px rgba(0,0,0,.08)}
  .selectors{display:flex;gap:4px;height:25px}
  .select{flex:1;border:1px solid #cfcfcf;font-size:9.5px;display:flex;align-items:center;justify-content:space-between;padding:0 8px 0 9px}
  .caret{width:0;height:0;border-left:4px solid transparent;border-right:4px solid transparent;border-top:4px solid #555}
  .segmented{display:flex;border:1px solid var(--line);margin-top:10px;height:26px}
  .segmented.period{margin-top:6px;height:28px}
  .segment{flex:1;display:flex;align-items:center;justify-content:center;font-size:9.5px;color:var(--text)}
  .segment.is-active{background:linear-gradient(#86c84a,#6fae30);color:#fff;font-weight:700}

  .spread-table{width:100%;border-collapse:collapse;margin-top:7px;font-size:8.5px}
  .spread-table + .spread-table{margin-top:5px}
  .spread-table td{border:1px solid var(--line);height:26px;text-align:center}
  .spread-table td.label{width:145px;background:var(--label-bg);font-weight:700}
  .load-more{height:26px;margin-top:4px;border:1px solid var(--line);background:#f7f7f8;font-size:9.5px;display:flex;align-items:center;justify-content:center;gap:7px}

  .section-band{margin:12px -5px 0;height:41px;background:var(--band);display:flex;align-items:center;justify-content:center;font-size:9px;font-weight:700;letter-spacing:.2px}
  .section-band.supply{color:var(--green)}
  .section-band.time{color:var(--orange);margin-top:14px}

  .gauge{position:relative;width:120px;height:120px;margin:6px auto 0}
  .gauge-value{position:absolute;left:0;right:0;top:38px;text-align:center;color:var(--green);font-size:30px;font-weight:300;line-height:1}
  .gauge-value sup{font-size:14px;vertical-align:top;position:relative;top:3px}
  .gauge-caption{position:absolute;left:0;right:0;top:72px;text-align:center;color:var(--green);font-size:6px}
  .insight-title{text-align:center;font-size:9.5px;font-weight:700;color:#555;margin-top:5px}
  .insight-text{text-align:center;font-size:7.4px;line-height:10px;color:#666;margin:6px 6px 0}
  .learn-more{display:block;text-align:center;font-size:7.5px;font-weight:700;color:var(--green);margin-top:12px}

  .chart{display:block;margin:8px 0 0;width:290px;height:135px}
  .chart text{font-family:"Roboto",Arial,sans-serif;font-size:6px;fill:#666}

  /* footer */
  .site-footer{text-align:center;padding-top:20px;font-size:7px;color:#666}
  .social{display:flex;justify-content:center;gap:13px;margin-top:8px}
  .social span{width:6px;height:6px;border-radius:50%;background:#9aa4ad}
  .footer-links{display:flex;justify-content:center;margin-top:11px;font-size:7.5px}
  .footer-links a{color:#555;text-decoration:none;padding:0 6px;border-left:1px solid #bbb}
  .footer-links a:first-child{border-left:0}
</style>
</head>
<body>
<div class="page">
  <header class="site-header">
    <div class="brand"><span class="brand-dot"></span><span class="brand-name">GasSpread</span></div>
    <div class="user-greeting">
      <svg width="8" height="8" viewBox="0 0 8 8" aria-hidden="true"><circle cx="4" cy="2.2" r="1.8" fill="#333"/><path d="M0.5 8 Q0.5 4.6 4 4.6 Q7.5 4.6 7.5 8Z" fill="#333"/></svg>
      Hi! User
    </div>
    <div class="options-btn">
      <svg width="9" height="9" viewBox="0 0 10 10" aria-hidden="true"><circle cx="5" cy="5" r="3.2" fill="none" stroke="#333" stroke-width="2.2" stroke-dasharray="1.6 1"/><circle cx="5" cy="5" r="1.2" fill="#333"/></svg>
      Options <span class="caret"></span>
    </div>
    <nav class="region-tabs">
      <div class="region-tab is-active">EAST</div>
      <div class="region-tab central">CENTRAL</div>
      <div class="region-tab west">WEST</div>
    </nav>
  </header>

  <main class="panel">
    <div class="selectors">
      <div class="select">Source Indices <span class="caret"></span></div>
      <div class="select">Destination Indices <span class="caret"></span></div>
    </div>
    <div class="segmented">
      <div class="segment">5 days</div>
      <div class="segment is-active">7 days</div>
      <div class="segment">18 days</div>
    </div>
    <div class="segmented period">
      <div class="segment">Month</div>
      <div class="segment is-active">Year</div>
    </div>

    <table class="spread-table">
      <tr><td class="label">Spread-name</td><td>Spread 1</td></tr>
      <tr><td class="label">Avg sprd</td><td>Item 1</td></tr>
      <tr><td class="label">+ve prob</td><td>- - - -</td></tr>
      <tr><td class="label">-ve prob</td><td>- - - -</td></tr>
      <tr><td class="label">Spike prob</td><td>- - - -</td></tr>
      <tr><td class="label">Avg supply</td><td>- - - -</td></tr>
      <tr><td class="label">Supply cut_prob</td><td>- - - -</td></tr>
    </table>
    <table class="spread-table">
      <tr><td class="label">Spread-name</td><td>Spread 2</td></tr>
      <tr><td class="label">Avg sprd</td><td>Item 2</td></tr>
      <tr><td class="label">+ve prob</td><td>- - - -</td></tr>
      <tr><td class="label">-ve prob</td><td>- - - -</td></tr>
      <tr><td class="label">Spike prob</td><td>- - - -</td></tr>
      <tr><td class="label">Avg supply</td><td>- - - -</td></tr>
      <tr><td class="label">Supply cut_prob</td><td>- - - -</td></tr>
    </table>
    <div class="load-more">Load More Items <span class="caret"></span></div>

    <div class="section-band supply">SPREAD V/S SUPPLY</div>
    <div class="gauge">
      <svg width="120" height="120" viewBox="0 0 120 120" aria-hidden="true">
        <circle cx="60" cy="60" r="52" fill="none" stroke="#ececec" stroke-width="4" stroke-dasharray="245 400" transform="rotate(135 60 60)"/>
        <circle cx="60" cy="60" r="52" fill="none" stroke="var(--green)" stroke-width="4" stroke-dasharray="118 400" transform="rotate(135 60 60)"/>
        <circle cx="60" cy="60" r="45" fill="none" stroke="var(--green-light)" stroke-width="2" stroke-dasharray="95 400" transform="rotate(135 60 60)"/>
        <circle cx="23.2" cy="96.8" r="5.5" fill="#fff" stroke="var(--green)" stroke-width="3"/>
        <circle cx="96.8" cy="96.8" r="5.5" fill="#fff" stroke="#e6e6e6" stroke-width="3"/>
      </svg>
      <div class="gauge-value">30<sup>%</sup></div>
      <div class="gauge-caption">SPREAD V/S SUPPLY</div>
    </div>
    <h3 class="insight-title">LOREM IPSUM DOLOR</h3>
    <p class="insight-text">Lorem ipsum dolor sit amet, consectetuer adipiscing elit, sed diam nonummy nibh euismod tincidunt ut laoreet dolore magna aliquam erat volutpat. Ut wisi enim ad minim veniam, quis nostrud exerci tation ullamcorper suscipit lobortis nisl ut aliquip ex ea commodo consequat.</p>
    <a class="learn-more" href="#">Learn more...</a>

    <div class="section-band time">SPREADS ACROSS TIME</div>
    <svg class="chart" viewBox="0 0 290 135" role="img" aria-label="Bar chart of spreads from 1 Dec 2013 to 1 Dec 2014">
      <g stroke="#ececec" stroke-width="0.6">
        <line x1="26" y1="18" x2="280" y2="18"/>
        <line x1="26" y1="38" x2="280" y2="38"/>
        <line x1="26" y1="58" x2="280" y2="58"/>
        <line x1="26" y1="78" x2="280" y2="78"/>
        <line x1="26" y1="98" x2="280" y2="98"/>
      </g>
      <line x1="26" y1="10" x2="26" y2="118" stroke="#cfcfcf" stroke-width="0.8"/>
      <line x1="26" y1="118" x2="280" y2="118" stroke="#cfcfcf" stroke-width="0.8"/>
      <text x="18" y="20">5</text><text x="18" y="40">4</text><text x="18" y="60">3</text><text x="18" y="80">2</text><text x="18" y="100">1</text>
      <g fill="var(--green-light)">
        <rect x="33" y="80" width="11" height="38"/><rect x="48" y="74" width="11" height="44"/>
        <rect x="63" y="74" width="11" height="44"/><rect x="78" y="74" width="11" height="44"/>
      </g>
      <g fill="var(--grey-bar)">
        <rect x="93" y="58" width="11" height="60"/><rect x="108" y="58" width="11" height="60"/>
        <rect x="123" y="58" width="11" height="60"/><rect x="138" y="58" width="11" height="60"/>
      </g>
      <g fill="var(--peach)">
        <rect x="153" y="46" width="11" height="72"/><rect x="168" y="38" width="11" height="80"/>
        <rect x="183" y="38" width="11" height="80"/><rect x="198" y="38" width="11" height="80"/>
      </g>
      <g fill="var(--orange)">
        <rect x="213" y="18" width="11" height="100"/><rect x="228" y="18" width="11" height="100"/>
        <rect x="243" y="18" width="11" height="100"/><rect x="258" y="18" width="11" height="100"/>
      </g>
      <text x="22" y="127">1- dec- 2013</text>
      <text x="236" y="127">1- dec- 2014</text>
    </svg>
  </main>

  <footer class="site-footer">
    <p>Copyright © 2014 GasSpread. All rights Reserved.</p>
    <div class="social">
      <span role="img" aria-label="Social link 1"></span>
      <span role="img" aria-label="Social link 2"></span>
      <span role="img" aria-label="Social link 3"></span>
    </div>
    <nav class="footer-links">
      <a href="#">Sitemap</a><a href="#">Contact us</a><a href="#">Privacy Policy</a><a href="#">Blog</a><a href="#">Help centre</a>
    </nav>
  </footer>
</div>
</body>
</html>
```